Direct Mail flyer for the timeshare industry.

We need someone who has experience in direct mail experience in postcards and successful campaigns. The post card we are using is not good at all.

We are looking at a 5.5 x 8.5 postcard with 4 color on one side and the black and white on the mailing side. But if someone has a better idea instead of a postcard then I am open to that

Target Market(s)

Timeshare owners...most of them are 55 plus in age. We help people get out of their time share

Industry/Entity Type

Industry

Font styles to use
Serif

Colors

Designer to choose colors to be used in the design.

Requirements
Must have
• Call to action and be easy to understand and look very professional and not fake or cheesy

```html
<!DOCTYPE html>
<html lang="en">
<head>
<meta charset="utf-8">
<title>Clearway Group – Private Event Postcard</title>
<link rel="stylesheet" href="https://fonts.googleapis.com/css2?family=Alegreya:ital,wght@0,400;0,700;0,800;1,400;1,700&family=Open+Sans:wght@400;600;700&family=Arimo&display=swap">
<style>
  :root{
    --page:#ebe8e3;
    --card:#ffffff;
    --navy:#2f6fa3;
    --blue-mid:#4a8cc2;
    --band:#5a9bd0;
    --teal:#7db9cb;
    --ribbon:#7fbccc;
    --yellow:#f5c024;
    --ink:#1e1e1e;
    --text-dark:#2a2a2a;
  }
  *{box-sizing:border-box;margin:0;padding:0}
  html,body{width:900px;height:1200px;overflow:hidden}
  body{background:var(--page);position:relative;font-family:"Alegreya",serif;color:var(--ink)}

  .postcard{position:absolute;left:75px;width:752px;height:487px;background:var(--card);overflow:hidden;box-shadow:0 4px 10px rgba(0,0,0,.18)}
  .postcard--front{top:68px}
  .postcard--mailing{top:588px}

  .scene-photo{position:absolute;inset:0;
    background:linear-gradient(180deg,#86c0e4 0%,#c9e2f1 38%,#a9d4e6 50%,#5fb0cf 62%,#3b9cc4 100%)}

  .header-bar{position:absolute;left:0;top:0;width:100%;height:77px;background:rgba(140,196,232,.55)}
  .header-rule{position:absolute;left:0;top:76px;width:430px;height:3px;background:#fff}
  .event-title{position:absolute;left:30px;top:32px;font-weight:800;font-size:23px;letter-spacing:1.2px;color:#fff;text-shadow:0 1px 2px rgba(0,0,0,.25)}

  .info-tab{position:absolute;left:0;width:66px;height:40px;background:var(--navy);border-radius:0 20px 20px 0;display:flex;align-items:center;justify-content:center;padding-left:10px}
  .info-tab--venue{top:97px}
  .info-tab--date{top:146px}
  .info-text{position:absolute;left:76px;color:var(--text-dark)}
  .info-text--venue{top:95px}
  .info-text--date{top:144px}
  .info-main{font-size:19px;line-height:22px}
  .info-sub{font-size:13.5px;line-height:17px}

  .seating-badge{position:absolute;left:427px;top:17px;width:110px;height:110px;border-radius:50%;background:var(--yellow);border:3px solid #fff;box-shadow:0 0 0 2px #3a3a3a;display:flex;flex-direction:column;align-items:center;justify-content:center;font-family:"Open Sans",sans-serif;color:#2a2a2a;z-index:3}
  .seating-badge__big{font-size:19px;font-weight:700;line-height:20px}
  .seating-badge__small{font-size:11px;font-weight:700;line-height:13px}

  .call-panel{position:absolute;left:535px;top:24px;width:217px;height:73px;background:var(--navy);font-family:"Open Sans",sans-serif;color:#fff;padding:14px 0 0 26px;z-index:2}
  .call-panel__label{font-size:20px;font-weight:600;letter-spacing:.5px;line-height:22px;border-bottom:2px solid #fff;width:165px;padding-bottom:2px}
  .call-panel__phone{font-size:20px;font-weight:700;line-height:26px}
  .rsvp-strip{position:absolute;left:535px;top:97px;width:217px;height:18px;background:var(--blue-mid);color:#fff;font-family:"Alegreya",serif;font-weight:700;font-size:11.5px;text-align:right;padding-right:28px;line-height:18px;z-index:2}
  .guarantee-strip{position:absolute;left:600px;top:115px;width:152px;height:14px;background:var(--yellow);font-family:"Open Sans",sans-serif;font-size:9.5px;line-height:14px;padding-left:10px;color:#222;z-index:2}

  .headline{position:absolute;left:172px;top:198px;font-weight:800;font-size:40px;color:var(--teal);letter-spacing:.3px}
  .invite-band{position:absolute;left:0;top:244px;width:588px;height:23px;background:var(--band);color:#fff;font-weight:700;font-size:13.5px;line-height:23px;padding-left:102px}

  .benefit{position:absolute;top:287px;width:178px;height:143px;background:rgba(255,255,255,.82);border:2px solid rgba(255,255,255,.95);border-radius:14px;text-align:center;padding:15px 12px 0}
  .benefit--education{left:23px}
  .benefit--protection{left:226px}
  .benefit--advisement{left:430px}
  .benefit__title{font-style:italic;font-weight:700;font-size:14px;letter-spacing:.4px;margin-bottom:5px}
  .benefit__copy{font-style:italic;font-size:10.8px;line-height:15px;color:#333}

  .free-ribbon{position:absolute;inset:0;pointer-events:none}

  .postage-indicia{position:absolute;left:622px;top:27px;width:94px;height:95px;border:2px dashed #222;font-family:"Arimo",sans-serif;font-size:11.5px;line-height:14.5px;text-align:center;padding-top:7px}
  .delivery-address{position:absolute;left:497px;top:145px;width:221px;height:63px;border:1.5px solid #222;font-family:"Arimo",sans-serif;font-size:14px;line-height:18px;padding:14px 0 0 8px}
  .return-address{position:absolute;left:25px;top:395px;font-size:15px;line-height:18px}
  .return-address__name{font-size:16px;line-height:20px}
</style>
</head>
<body>

<section class="postcard postcard--front" aria-label="Event invitation, front side">
  <div class="scene-photo" role="img" aria-label="Photo of an infinity pool overlooking the sea under a blue sky, with glass doors of a modern villa on the right"></div>

  <div class="header-bar"></div>
  <div class="header-rule"></div>
  <h1 class="event-title">A PRIVATE EVENT INVITATION</h1>

  <div class="info-tab info-tab--venue">
    <svg width="20" height="26" viewBox="0 0 20 26" aria-hidden="true"><path d="M10 1C5 1 1.5 4.7 1.5 9.3 1.5 15.5 10 25 10 25s8.5-9.5 8.5-15.7C18.5 4.7 15 1 10 1z" fill="#fff"/><circle cx="10" cy="9.5" r="3.4" fill="#2f6fa3"/></svg>
  </div>
  <div class="info-text info-text--venue">
    <div class="info-main">Harbor View Suites</div>
    <div class="info-sub">2150 Meadow Parkway, Fort Worth, TX 76137</div>
  </div>

  <div class="info-tab info-tab--date">
    <svg width="28" height="26" viewBox="0 0 28 26" aria-hidden="true"><rect x="2" y="4" width="24" height="20" rx="3" fill="none" stroke="#fff" stroke-width="2.4"/><rect x="2" y="4" width="24" height="5" fill="#fff"/><rect x="7" y="1" width="2.5" height="6" rx="1" fill="#fff"/><rect x="18.5" y="1" width="2.5" height="6" rx="1" fill="#fff"/><g fill="#fff"><rect x="6" y="12" width="4" height="3"/><rect x="12" y="12" width="4" height="3"/><rect x="18" y="12" width="4" height="3"/><rect x="6" y="17" width="4" height="3"/><rect x="12" y="17" width="4" height="3"/><rect x="18" y="17" width="4" height="3"/></g></svg>
  </div>
  <div class="info-text info-text--date">
    <div class="info-main">Saturday, February 17, 2018</div>
    <div class="info-sub">10:30 AM | 3:00 PM | 6:00 PM</div>
  </div>

  <div class="seating-badge">
    <span class="seating-badge__big">LIMITED</span>
    <span class="seating-badge__small">SEATING</span>
  </div>

  <div class="call-panel">
    <div class="call-panel__label">CALL TODAY</div>
    <div class="call-panel__phone">(888) 555-0147</div>
  </div>
  <div class="rsvp-strip">with RSVP Code # CWG70218</div>
  <div class="guarantee-strip">to guarantee your seats!</div>

  <h2 class="headline">This is your chance!</h2>
  <p class="invite-band">We’ve arranged for you and one guest to attend our Clearway Group Event</p>

  <article class="benefit benefit--education">
    <h3 class="benefit__title">EDUCATION</h3>
    <p class="benefit__copy">We promise this event will be an eye-opening experience and an incredible learning opportunity regardless of your current situation.</p>
  </article>
  <article class="benefit benefit--protection">
    <h3 class="benefit__title">PROTECTION</h3>
    <p class="benefit__copy">Arm yourself with the knowledge of how to avoid the current scams occurring in the timeshare industry to protect you as an owner.</p>
  </article>
  <article class="benefit benefit--advisement">
    <h3 class="benefit__title">ADVISEMENT</h3>
    <p class="benefit__copy">Your questions are welcomed and will be addressed. This will bring you the sense of confidence that you have been seeking.</p>
  </article>

  <svg class="free-ribbon" width="752" height="487" viewBox="0 0 752 487" aria-hidden="true">
    <polygon points="752,318 752,340 578,487 555,487" fill="#fff"/>
    <polygon points="752,345 752,410 662,487 585,487" fill="var(--ribbon)"/>
    <g transform="translate(700,430) rotate(-42)" fill="#fff" font-family="Open Sans, sans-serif" text-anchor="middle">
      <text x="0" y="-6" font-size="25" font-weight="700">FREE</text>
      <text x="0" y="15" font-size="17" font-weight="600">OF CHARGE</text>
    </g>
  </svg>
</section>

<section class="postcard postcard--mailing" aria-label="Postcard mailing side">
  <div class="postage-indicia">PRSRT STD<br>ECRWSS<br>U.S. POSTAGE<br>PAID<br>EDDM RETAIL</div>
  <div class="delivery-address">Local<br>Postal Customer</div>
  <address class="return-address" style="font-style:normal">
    <div class="return-address__name">Clearway Group, LLC</div>
    920 Maple Ridge Drive<br>
    Springfield, Mo. 65804
  </address>
</section>

</body>
</html>
```